Fitness Business Card Design Needed

We are looking for a business card design that stands out but is also simple and unique. I like the idea of on one side using the picture of myself with my logo at my feet. I love the texture on the business card so please take that into account when designing. Then on the other side having my contact details. I want it to be clean, modern, and pretty. I am open to designs that allow spot gloss or gold foiling.

Space for Name, Phone number, email, and website

```html
<!DOCTYPE html>
<html lang="en">
<head>
<meta charset="utf-8">
<title>Kestrel Coaching – Business Cards</title>
<link rel="stylesheet" href="https://fonts.googleapis.com/css2?family=Montserrat:wght@400;500&family=Open+Sans:wght@400&display=swap">
<style>
  :root {
    --backdrop: #e6e6e6;
    --card-black: #0d0d0d;
    --card-white: #f7f7f5;
    --gold-light: #e6bf6a;
    --gold-mid: #c8963c;
    --ink: #2b2b2b;
    --gold-sheen: linear-gradient(100deg, #a97b2c 0%, #e2c074 35%, #c99a45 60%, #f0d38e 80%, #b0842f 100%);
  }
  * { box-sizing: border-box; margin: 0; padding: 0; }
  html, body { width: 1200px; height: 1200px; overflow: hidden; }
  body {
    background: var(--backdrop);
    display: flex;
    align-items: center;
    justify-content: center;
    gap: 100px;
    font-family: "Open Sans", sans-serif;
  }
  .card {
    width: 400px;
    height: 700px;
    position: relative;
    overflow: hidden;
    background: var(--card-black);
    box-shadow: 0 18px 40px rgba(0,0,0,0.25);
  }

  /* Brand name: plain text, one colour, one weight */
  .brand {
    display: flex;
    align-items: center;
    gap: 10px;
    font-family: "Montserrat", sans-serif;
    font-weight: 500;
    font-size: 24px;
    white-space: nowrap;
  }
  .brand-square {
    width: 12px;
    height: 12px;
    background: currentColor;
    flex: none;
  }

  /* Contact side */
  .contact-top {
    height: 260px;
    background: var(--card-white);
    display: flex;
    align-items: center;
    justify-content: center;
    padding-bottom: 50px;
  }
  .contact-top .brand { color: var(--ink); }
  .divider-mark {
    position: absolute;
    top: 200px;
    left: 50%;
    transform: translateX(-50%);
  }
  .contact-body {
    text-align: center;
    color: var(--gold-light);
    padding-top: 110px;
  }
  .person-name { font-size: 22px; letter-spacing: 0.5px; }
  .person-role { font-size: 11px; margin-top: 2px; }
  .bullet { margin: 16px auto; display: block; }
  .contact-line { font-size: 15px; line-height: 1.6; }

  /* Photo side */
  .photo-area {
    position: absolute;
    left: 90px;
    top: 40px;
    width: 220px;
    height: 500px;
    border-radius: 40px 40px 10px 10px;
    background: radial-gradient(ellipse at 50% 40%, #c98f6f 0%, #8a5a44 45%, #2a1c16 80%, var(--card-black) 100%);
  }
  .brand-band {
    position: absolute;
    left: 0;
    right: 0;
    bottom: 0;
    height: 150px;
    background: var(--gold-sheen);
    display: flex;
    align-items: center;
    justify-content: center;
  }
  .brand-band .brand { color: var(--ink); font-size: 28px; }
</style>
</head>
<body>
  <article class="card card--contact">
    <header class="contact-top">
      <div class="brand"><span class="brand-square"></span>Kestrel Coaching</div>
    </header>
    <svg class="divider-mark" width="120" height="120" viewBox="0 0 120 120" aria-hidden="true">
      <defs>
        <linearGradient id="goldFill" x1="0" y1="0" x2="1" y2="1">
          <stop offset="0" stop-color="#a97b2c"/>
          <stop offset="0.45" stop-color="#e2c074"/>
          <stop offset="1" stop-color="#b0842f"/>
        </linearGradient>
      </defs>
      <rect x="25" y="25" width="70" height="70" fill="url(#goldFill)" transform="rotate(45 60 60)"/>
    </svg>
    <section class="contact-body">
      <div class="person-name">Lena R. Hollis</div>
      <div class="person-role">Trainer</div>
      <svg class="bullet" width="12" height="12" viewBox="0 0 12 12" aria-hidden="true"><rect x="2" y="2" width="8" height="8" fill="none" stroke="#c8963c" transform="rotate(45 6 6)"/></svg>
      <div class="contact-line">Dummy city</div>
      <div class="contact-line">Dummy Country Land</div>
      <svg class="bullet" width="12" height="12" viewBox="0 0 12 12" aria-hidden="true"><rect x="2" y="2" width="8" height="8" fill="none" stroke="#c8963c" transform="rotate(45 6 6)"/></svg>
      <div class="contact-line">1-555-018240</div>
      <div class="contact-line">hello@kestrelcoaching.com</div>
      <div class="contact-line">www.kestrelcoaching.com</div>
    </section>
  </article>

  <article class="card card--photo">
    <div class="photo-area" role="img" aria-label="Full-length photo of the trainer in a red bikini, standing on a rock"></div>
    <footer class="brand-band">
      <div class="brand"><span class="brand-square"></span>Kestrel Coaching</div>
    </footer>
  </article>
</body>
</html>
```